Powerpoint for Travio

Check out the attached sample powerpoint, we would like our powerpoint to look similar to this. in the slides where you see monitor, we would like to put pics of different industries in each monitor. like images of hotels, hospitals, large business with multiple locations, small business, retail)

The Powerpoint will contain the below slides

About US
Our Guarantee – 100% satisfaction and 30% cost savings
Products & Services ( Hosted PBX phone system, SIP Trunking, Network security solutions, commercial grade band width and firewalls, IT Network design services)
Features ( One slide for this we will enter the content)
Industries ( Small business, hospitality, hospitals, Banks for secure voice, Large business with multiple locations, Retail)
Hosted PBX
Why Travio
Channel partners
Our customers
Contact us
Updates

Target Market(s)

Small business, hospitality, hospitals, Banks for secure voice, Large business with multiple locations, Retail, law firms, insurance companies

Industry/Entity Type

Security

Requirements
Must have
• Please look at the attached powerpoint for color, style, font details

```html
<!DOCTYPE html>
<html lang="en">
<head>
<meta charset="utf-8">
<title>Presentation Slides</title>
<link href="https://fonts.googleapis.com/css2?family=Graduate&family=Cinzel:wght@400;700&display=swap" rel="stylesheet">
<style>
  :root {
    --page: #ffffff;
    --slide-light: #e9e9e9;
    --slide-dark: #cfcfcf;
    --brand-blue: #29abe2;
    --brand-blue-deep: #1b75bb;
    --ink: #2b2b2b;
    --rule: #3a3a3c;
    --muted: #555555;
    --white: #ffffff;
  }
  * { margin: 0; padding: 0; box-sizing: border-box; }
  html, body { width: 1200px; height: 900px; overflow: hidden; background: var(--page); }
  .canvas { position: relative; width: 1200px; height: 900px; }
  h2, h3 { font-weight: 400; }

  .slide {
    position: absolute;
    width: 557px; height: 313px;
    background: linear-gradient(160deg, var(--slide-light) 0%, #dedede 50%, var(--slide-dark) 100%);
    overflow: hidden;
  }
  .slide--graphic { left: 18px; top: 137px; }
  .slide--bullets { left: 609px; top: 149px; width: 556px; height: 312px; }
  .slide--content { left: 18px; top: 473px; }
  .slide--thanks  { left: 609px; top: 485px; height: 312px; }

  .slide-title {
    position: absolute; left: 34px; top: 16px;
    font-family: "Graduate", serif;
    font-size: 28px; line-height: 1;
    color: var(--brand-blue);
    -webkit-text-stroke: 1.2px var(--brand-blue);
    letter-spacing: 0.3px;
  }
  .title-rule { position: absolute; left: 0; top: 42px; width: 500px; height: 22px; }
  .page-flag { position: absolute; right: 10px; top: 10px; width: 50px; height: 48px; }
  .page-number {
    position: absolute; right: 16px; top: 17px;
    font-family: "Graduate", serif; font-size: 11px; color: var(--white);
  }

  .tagline {
    position: absolute; left: 0; right: 0; bottom: 8px;
    text-align: center;
    font-family: "Cinzel", serif; font-size: 7.5px; color: var(--muted);
    letter-spacing: 0.2px;
  }

  .chart { position: absolute; left: 0; top: 0; width: 557px; height: 313px; }

  /* bullets slide */
  .column-heading {
    position: absolute;
    font-family: "Cinzel", serif; font-size: 20px; color: var(--ink);
  }
  .column-heading--bullets { left: 62px; top: 74px; }
  .column-heading--table { left: 395px; top: 74px; }
  .main-bullet {
    position: absolute; left: 52px; top: 125px;
    display: flex; align-items: center; gap: 5px;
    font-family: "Graduate", serif; font-size: 11px; color: var(--brand-blue);
    -webkit-text-stroke: 0.4px var(--brand-blue);
  }
  .main-bullet::before {
    content: ""; width: 7px; height: 7px; border-radius: 50%;
    border: 1.6px solid var(--brand-blue);
  }
  .sub-list {
    position: absolute; top: 141px;
    list-style: none;
    font-family: "Cinzel", serif; font-size: 6px; color: var(--ink);
  }
  .sub-list--left { left: 74px; }
  .sub-list--right { left: 152px; }
  .sub-list li { display: flex; align-items: center; gap: 4px; height: 14.5px; }
  .sub-list li::before {
    content: ""; width: 7px; height: 7px; border-radius: 50%;
    background: var(--brand-blue); border: 1.2px solid var(--rule);
  }
  .column-divider { position: absolute; left: 279px; top: 86px; width: 2px; height: 199px; background: var(--brand-blue); }
  .data-table {
    position: absolute; left: 326px; top: 104px; width: 202px; height: 167px;
    border-collapse: collapse; border: 4px solid var(--brand-blue);
    background: var(--white);
  }
  .data-table td { border: 3px solid var(--brand-blue); }
  .data-table tr:first-child td { height: 42px; }

  /* content slide */
  .content-title {
    position: absolute; left: 25px; top: 76px;
    font-family: "Cinzel", serif; font-size: 15px; color: var(--ink);
  }
  .lead-arrow { position: absolute; left: 24px; top: 98px; width: 20px; height: 16px; }
  .body-copy {
    position: absolute;
    font-family: "Cinzel", serif; font-size: 4.6px; line-height: 6.2px; color: var(--muted);
  }
  .body-copy--lead { left: 50px; top: 97px; width: 310px; }
  .body-copy--1 { left: 25px; top: 138px; width: 335px; }
  .body-copy--2 { left: 25px; top: 175px; width: 335px; }
  .body-copy--3 { left: 25px; top: 212px; width: 335px; }

  /* thanks slide */
  .thanks {
    position: absolute; left: 0; right: 0; top: 128px;
    text-align: center;
    font-family: "Graduate", serif; font-size: 46px; line-height: 48px;
    color: var(--brand-blue);
    -webkit-text-stroke: 2.4px var(--brand-blue);
    letter-spacing: -1px;
  }
  .thanks--reflection {
    top: 174px;
    transform: scaleY(-1);
    opacity: 0.35;
    -webkit-mask-image: linear-gradient(to top, rgba(0,0,0,1) 0%, rgba(0,0,0,0) 60%);
            mask-image: linear-gradient(to top, rgba(0,0,0,1) 0%, rgba(0,0,0,0) 60%);
  }
  .close-flag { position: absolute; right: 12px; bottom: 17px; width: 48px; height: 48px; }
</style>
</head>
<body>
<main class="canvas">

  <!-- Graphic slide -->
  <section class="slide slide--graphic">
    <h2 class="slide-title">GRAPHIC SLIDE</h2>
    <svg class="title-rule" viewBox="0 0 500 22" aria-hidden="true">
      <line x1="14" y1="11" x2="487" y2="11" stroke="#3a3a3c" stroke-width="2"/>
      <rect x="13" y="4" width="14" height="14" rx="4" transform="rotate(45 20 11)" fill="none" stroke="#3a3a3c" stroke-width="1.6"/>
      <circle cx="20" cy="11" r="3.6" fill="#29abe2"/>
    </svg>
    <svg class="page-flag" viewBox="0 0 50 48" aria-hidden="true"><polygon points="0,0 50,0 50,48" fill="#29abe2"/></svg>
    <span class="page-number">04</span>

    <svg class="chart" viewBox="0 0 557 313" role="img" aria-label="Three tier pyramid and pie chart">
      <polygon points="25,245 270,245 270,258 25,258" fill="#3a3a3c"/>
      <polygon points="45,206 226,206 270,245 25,245" fill="#58595b"/>
      <polygon points="87,203 225,203 225,206 87,206" fill="#1b75bb"/>
      <polygon points="80,161 204,161 225,203 69,203" fill="#29abe2"/>
      <polygon points="112,155 179,155 179,161 112,161" fill="#39b54a"/>
      <polygon points="145,118 179,155 112,155" fill="#8dc63f"/>
      <path d="M470.9,186 A75,75 0 0 1 434.5,238 L434.5,250 A75,75 0 0 0 470.9,198 Z" fill="#1b75bb"/>
      <path d="M472,173 A75,75 0 0 1 470.9,186 L470.9,198 A75,75 0 0 0 472,185 Z" fill="#1b75bb"/>
      <path d="M434.5,238 A75,75 0 0 1 354,234.4 L354,246.4 A75,75 0 0 0 434.5,250 Z" fill="#9c6d3f"/>
      <path d="M354,234.4 A75,75 0 0 1 322,173 L322,185 A75,75 0 0 0 354,246.4 Z" fill="#3a3a3c"/>
      <g stroke="#ffffff" stroke-width="2" stroke-linejoin="round">
        <path d="M397,173 L397,98 A75,75 0 0 1 458.4,130 Z" fill="#2db87a"/>
        <path d="M397,173 L458.4,130 A75,75 0 0 1 470.9,186 Z" fill="#16a99a"/>
        <path d="M397,173 L470.9,186 A75,75 0 0 1 434.5,238 Z" fill="#29abe2"/>
        <path d="M397,173 L434.5,238 A75,75 0 0 1 354,234.4 Z" fill="#c4966a"/>
        <path d="M397,173 L354,234.4 A75,75 0 0 1 324.6,153.6 Z" fill="#6d6e71"/>
        <path d="M397,173 L324.6,153.6 A75,75 0 0 1 354,111.6 Z" fill="#8dc63f"/>
        <path d="M397,173 L354,111.6 A75,75 0 0 1 397,98 Z" fill="#0e9a48"/>
      </g>
    </svg>
    <p class="tagline">A Cloud Based Carrier Grade Communications and Solutions Provider</p>
  </section>

  <!-- Bullets and table slide -->
  <section class="slide slide--bullets">
    <h2 class="slide-title">SLIDE TITLE</h2>
    <svg class="title-rule" viewBox="0 0 500 22" aria-hidden="true">
      <line x1="14" y1="11" x2="487" y2="11" stroke="#3a3a3c" stroke-width="2"/>
      <rect x="13" y="4" width="14" height="14" rx="4" transform="rotate(45 20 11)" fill="none" stroke="#3a3a3c" stroke-width="1.6"/>
      <circle cx="20" cy="11" r="3.6" fill="#29abe2"/>
    </svg>
    <svg class="page-flag" viewBox="0 0 50 48" aria-hidden="true"><polygon points="0,0 50,0 50,48" fill="#29abe2"/></svg>
    <span class="page-number">04</span>

    <h3 class="column-heading column-heading--bullets">Bullet Form</h3>
    <p class="main-bullet">MAIN BULLET</p>
    <ul class="sub-list sub-list--left">
      <li>SUB BULLET FORM</li><li>SUB BULLET FORM</li><li>SUB BULLET FORM</li>
      <li>SUB BULLET FORM</li><li>SUB BULLET FORM</li><li>SUB BULLET FORM</li>
    </ul>
    <ul class="sub-list sub-list--right">
      <li>SUB BULLET FORM</li><li>SUB BULLET FORM</li><li>SUB BULLET FORM</li>
      <li>SUB BULLET FORM</li><li>SUB BULLET FORM</li><li>SUB BULLET FORM</li>
    </ul>

    <div class="column-divider"></div>

    <h3 class="column-heading column-heading--table">Table</h3>
    <table class="data-table">
      <tr><td></td><td></td></tr>
      <tr><td></td><td></td></tr>
      <tr><td></td><td></td></tr>
      <tr><td></td><td></td></tr>
      <tr><td></td><td></td></tr>
      <tr><td></td><td></td></tr>
    </table>
  </section>

  <!-- Content slide -->
  <section class="slide slide--content">
    <h2 class="slide-title">SLIDE TITLE</h2>
    <svg class="title-rule" viewBox="0 0 500 22" aria-hidden="true">
      <line x1="14" y1="11" x2="487" y2="11" stroke="#3a3a3c" stroke-width="2"/>
      <rect x="13" y="4" width="14" height="14" rx="4" transform="rotate(45 20 11)" fill="none" stroke="#3a3a3c" stroke-width="1.6"/>
      <circle cx="20" cy="11" r="3.6" fill="#29abe2"/>
    </svg>
    <svg class="page-flag" viewBox="0 0 50 48" aria-hidden="true"><polygon points="0,0 50,0 50,48" fill="#29abe2"/></svg>
    <span class="page-number">04</span>

    <h3 class="content-title">Content Title</h3>
    <svg class="lead-arrow" viewBox="0 0 20 16" aria-hidden="true">
      <polygon points="0,0 10,0 18,8 10,16 0,16 8,8" fill="#1b75bb"/>
    </svg>
    <p class="body-copy body-copy--lead">Our network keeps every call clear and every line secure. We host voice, data and firewall services from carrier grade sites, so your teams stay connected across every office. Plans scale with you, support answers day and night, and upgrades arrive without new hardware on site. One partner handles lines, bandwidth, security and design, so you deal with one team, one contract and one simple monthly bill for every location you run today and tomorrow.</p>
    <p class="body-copy body-copy--1">Hosted PBX moves your phone system to the cloud. Staff keep their numbers, forward calls to mobiles and join meetings from any desk. Billing is one simple monthly line, and our engineers watch quality around the clock to catch faults before callers notice them. Voicemail arrives by email, menus change in minutes, and new users are added from a browser. Hotels, clinics, shops and law firms all run on the same platform with settings tuned to the way they work each day.</p>
    <p class="body-copy body-copy--2">SIP trunking links your existing equipment to our network and cuts long distance costs. Each trunk carries many calls at once, grows with demand and fails over to a backup route when a line drops, so customers always reach a person. Numbers move with you when you open a new site, and reports show call volume, peak hours and missed calls so managers can plan staff. Setup takes days rather than weeks and our team stays on the line until every test call connects.</p>
    <p class="body-copy body-copy--3">Network security covers firewalls, encrypted voice for banks and monitoring for hospitals and hotels. We design each network, install it, test it and document it, then stay on as your partner for updates, audits and new locations as you grow. Commercial grade bandwidth keeps video, payments and records moving, while alerts warn us of threats before they reach your staff. Every plan carries our satisfaction guarantee and clear savings against your current provider from the very first month.</p>
    <p class="tagline">A Cloud Based Carrier Grade Communications and Solutions Provider</p>
  </section>

  <!-- Closing slide -->
  <section class="slide slide--thanks">
    <p class="thanks">THANK YOU</p>
    <p class="thanks thanks--reflection" aria-hidden="true">THANK YOU</p>
    <svg class="close-flag" viewBox="0 0 48 48" aria-hidden="true"><polygon points="0,48 48,0 48,48" fill="#29abe2"/></svg>
    <p class="tagline">A Cloud Based Carrier Grade Communications and Solutions Provider</p>
  </section>

</main>
</body>
</html>
```